menu board design: stellar grill

we are a burger restaurant.
we need to re design our menu board to fit within the new design of the restaurant. we are after something simple and easy to read. the overall look and feel of the design should be inline with the design of the shop.

Target Market(s)

18-40 male and female

Colors

Designer to choose colors to be used in the design.

Requirements
Must have
• easy to read. good layout. white background. branding included in design.

```html
<!DOCTYPE html>
<html lang="en">
<head>
<meta charset="utf-8">
<title>Stellar Grill Menu Board</title>
<link href="https://fonts.googleapis.com/css2?family=Bangers&family=Exo+2:wght@400;600;700;800&family=Montserrat:wght@500&display=swap" rel="stylesheet">
<style>
  :root {
    --blue: #1c4c97;
    --yellow: #e3b61f;
    --yellow-soft: #f3e3a6;
    --red: #c1272d;
    --ink: #333333;
    --paper: #fbfbf9;
  }
  * { margin: 0; padding: 0; box-sizing: border-box; }
  html, body { width: 1200px; height: 600px; overflow: hidden; background: var(--paper); }
  .board {
    position: relative; width: 1200px; height: 600px; overflow: hidden;
    background: var(--paper); font-family: "Exo 2", sans-serif; color: var(--ink);
  }
  .edge { position: absolute; top: 0; height: 600px; background: var(--blue); }
  .edge--left { left: 0; width: 28px; }
  .edge--right { right: 0; width: 30px; }

  .brand {
    position: absolute; left: 90px; top: 90px; width: 290px; text-align: center;
    font-family: "Exo 2", sans-serif; font-weight: 800; color: var(--blue);
    font-size: 74px; line-height: 0.95;
  }
  .tagline {
    position: absolute; left: 80px; top: 322px; width: 300px; text-align: center;
    font-family: "Montserrat", sans-serif; font-weight: 500; font-size: 14px;
    letter-spacing: 5.5px; color: var(--blue);
  }
  .hero-art {
    position: absolute; left: 70px; top: 345px; width: 290px; height: 245px;
    background: radial-gradient(circle at 50% 45%, var(--yellow-soft) 0%, rgba(243,227,166,0.5) 55%, rgba(251,251,249,0) 75%);
  }

  .banner {
    position: absolute; font-family: "Bangers", sans-serif; text-align: center;
    background: var(--yellow); color: var(--blue); letter-spacing: 1px;
  }
  .banner--section { font-size: 31px; line-height: 32px; height: 32px; }
  .banner--sides { font-size: 36px; line-height: 38px; height: 38px; }
  .banner--sub { font-size: 21px; line-height: 27px; height: 27px; color: var(--red); }
  .banner--step {
    font-family: "Exo 2", sans-serif; font-weight: 700; font-size: 11.5px;
    line-height: 17px; height: 17px; letter-spacing: 0;
  }

  .menu-col { position: absolute; top: 60px; width: 316px; }
  .menu-col--beef { left: 439px; }
  .menu-col--chicken { left: 807px; }
  .intro { font-size: 11.5px; line-height: 14.5px; text-align: center; color: var(--ink); }
  .add-on {
    margin-top: 9px; font-weight: 700; font-size: 12px; color: var(--blue);
    text-align: center; letter-spacing: 0.3px;
  }
  .item { position: absolute; left: 0; width: 316px; }
  .item-row, .price-row {
    display: flex; align-items: baseline; color: var(--yellow); font-weight: 600;
    font-size: 12px; line-height: 14px; letter-spacing: 0.3px;
  }
  .leader { flex: 1; border-bottom: 1.5px dotted var(--yellow); margin: 0 2px 3px 3px; }
  .desc { font-size: 10px; line-height: 12.5px; color: var(--ink); text-align: justify; text-align-last: left; margin-top: 1px; }

  .rule { position: absolute; top: 362px; border-top: 2px dashed var(--blue); }

  .step-head {
    position: absolute; font-weight: 700; font-size: 12px; color: var(--blue);
    text-align: center; letter-spacing: 0.3px;
  }
  .choice { position: absolute; left: 432px; width: 179px; }
  .choice .price-row { line-height: 14.5px; }
  .toppings {
    position: absolute; left: 619px; top: 501px; width: 162px; font-size: 11px;
    line-height: 14.5px; color: var(--yellow); text-align: justify;
  }
  .toppings strong { font-weight: 700; letter-spacing: 0.3px; }

  .ribs-desc {
    position: absolute; left: 820px; top: 432px; width: 330px; text-align: center;
    font-size: 10.5px; line-height: 13.5px; color: var(--ink);
  }
  .packs { position: absolute; left: 828px; top: 486px; width: 158px; }
  .packs .price-row { margin-bottom: 15px; }
  .sauce {
    position: absolute; left: 1022px; top: 486px; font-weight: 700; font-size: 12px;
    line-height: 14.5px; color: var(--blue); letter-spacing: 0.3px;
  }
  .badge { position: absolute; left: 1038px; top: 520px; }
</style>
</head>
<body>
<main class="board">
  <div class="edge edge--left"></div>
  <div class="edge edge--right"></div>

  <h1 class="brand">Stellar<br>Grill</h1>
  <p class="tagline">CLASSICS FOR A REASON</p>
  <div class="hero-art" role="img" aria-label="Sketched drink glass and burger over a large pale yellow star"></div>

  <h2 class="banner banner--section" style="left:494px; top:26px; width:206px;">BEEF BURGERS</h2>
  <section class="menu-col menu-col--beef" style="height:270px;">
    <p class="intro">All our patties are 100% natural beef. We know because we grind it ourselves, smashed to order on a hot grill rite in from of you</p>
    <p class="add-on">DOUBLE PATTY ADD 4</p>
    <div class="item" style="top:71px;">
      <div class="item-row"><span>CLASSIC BEEF</span><span class="leader"></span><span>8.9</span></div>
      <p class="desc">Shredded lettuce, sliced tomato, caramelised onions, beetroot and BBQ sauce on a buttered sesame seed bum.</p>
    </div>
    <div class="item" style="top:123px;">
      <div class="item-row"><span>CHEESE BURGER</span><span class="leader"></span><span>9.5</span></div>
      <p class="desc">Dill pickles, minced onion, american cheese, mustard and ketchup on soft milk bun.</p>
    </div>
    <div class="item" style="top:170px;">
      <div class="item-row"><span>FLAME GRILL</span><span class="leader"></span><span>9.5</span></div>
      <p class="desc">Shredded lettuce, sliced tomato, minced onion, dill pickles, american cheese, mayo and ketchup on a soft bun.</p>
    </div>
    <div class="item" style="top:218px;">
      <div class="item-row"><span>BIG MIC</span><span class="leader"></span><span>9.9</span></div>
      <p class="desc">Shredded lettuce, dil pickles, minced onion, american cheese and special sauce on a soft milk bun.</p>
    </div>
  </section>

  <h2 class="banner banner--section" style="left:815px; top:27px; width:265px;">CHICKEN BURGERS</h2>
  <section class="menu-col menu-col--chicken" style="top:61px; height:270px;">
    <p class="intro">All our patties are 100% natural beef. We know because we grind it ourselves, smashed to order on a hot grill rite in from of you</p>
    <p class="add-on" style="margin-top:8px;">DOUBLE PATTY ADD 4</p>
    <div class="item" style="top:70px;">
      <div class="item-row"><span>CLASSIC BEEF</span><span class="leader"></span><span>8.9</span></div>
      <p class="desc">Shredded lettuce, sliced tomato, caramelised onions, beetroot and BBQ sauce on a buttered sesame seed bum.</p>
    </div>
    <div class="item" style="top:122px;">
      <div class="item-row"><span>CHEESE BURGER</span><span class="leader"></span><span>9.5</span></div>
      <p class="desc">Dill pickles, minced onion, american cheese, mustard and ketchup on soft milk bun.</p>
    </div>
    <div class="item" style="top:169px;">
      <div class="item-row"><span>FLAME GRILL</span><span class="leader"></span><span>9.5</span></div>
      <p class="desc">Shredded lettuce, sliced tomato, minced onion, dill pickles, american cheese, mayo and ketchup on a soft bun.</p>
    </div>
    <div class="item" style="top:217px;">
      <div class="item-row"><span>TRUFFLED</span><span class="leader"></span><span>9.9</span></div>
      <p class="desc">Rocket, caramelised onion, dill pickles, havarti cheese and truffle infused mayo on a soft milk bun.</p>
    </div>
  </section>

  <div class="rule" style="left:427px; width:260px;"></div>
  <h2 class="banner banner--sides" style="left:708px; top:345px; width:135px;">SIDES</h2>
  <div class="rule" style="left:855px; width:275px;"></div>

  <h3 class="banner banner--sub" style="left:462px; top:386px; width:228px;">NACHOS &amp; LOADED FRIES</h3>
  <span class="banner banner--step" style="left:484px; top:443px; width:74px;">STEP ONE</span>
  <span class="banner banner--step" style="left:660px; top:443px; width:73px;">STEP TWO</span>
  <p class="step-head" style="left:461px; top:472px; width:120px;">CHOOSE EITHER,</p>
  <p class="step-head" style="left:640px; top:472px; width:120px;">CHOOSE ONE,</p>

  <div class="choice" style="top:501px;">
    <div class="price-row"><span>SEASONED FRIES</span><span class="leader"></span><span>9.9</span></div>
  </div>
  <div class="choice" style="top:530px;">
    <div class="price-row"><span>OR FRESHLY COOKED</span></div>
    <div class="price-row"><span>CORN CHIPS</span><span class="leader"></span><span>11.5</span></div>
  </div>
  <p class="toppings"><strong>GUACAMOLE</strong> salsa fresca, guacamole, jalapeñoz, cheese sauce and sour cream. <strong>BEEF CHILLI</strong> salsa fresca, beef chilli, jalapeños, cheese sauce and sour cream.</p>

  <h3 class="banner banner--sub" style="left:890px; top:385px; width:227px;">BUFFALO CHICKEN RIBS</h3>
  <p class="ribs-desc">Buffalo style fried chicken ribs smothered in one dur mouth-watering sauce. Served with a side of ranch sauce.</p>
  <div class="packs">
    <div class="price-row"><span>6 PACK</span><span class="leader"></span><span>6.9</span></div>
    <div class="price-row"><span>12 PACK</span><span class="leader"></span><span>12.9</span></div>
    <div class="price-row"><span>24 PACK</span><span class="leader"></span><span>23.9</span></div>
  </div>
  <p class="sauce">CLASSIC HOT SAUCE<br>OR SMOKY BBQ</p>
  <svg class="badge" width="72" height="72" viewBox="0 0 72 72" aria-hidden="true">
    <circle cx="36" cy="36" r="32" fill="none" stroke="var(--blue)" stroke-width="2"/>
  </svg>
</main>
</body>
</html>
```